RB Larks Film Festival Poster

Design a poster for our film festival at the Redbrook University. We would like a graphic clean feel (examples attached).

Must have the following text:

18TH ANNUAL LARKS FILM FESTIVAL
MAY 1, 2 & 3 2015
OTTO VRELAND CINEMA
SCHOOL OF SCREEN AND DIGITAL STORYTELLING
REDBROOK UNIVERSITY
www.larksreelweek.example

Size:
8.5 x 10

Adobe Illustrator please.

Target Market(s)

We will print to poster size and will print to magazines.

Industry/Entity Type

Festival

Colors

Designer to choose colors to be used in the design.

```html
<!DOCTYPE html>
<html lang="en">
<head>
<meta charset="utf-8">
<title>18th Annual Larks Film Festival</title>
<link rel="stylesheet" href="https://fonts.googleapis.com/css2?family=Advent+Pro:wght@200;300&family=Oswald:wght@500;600&display=swap">
<style>
  :root {
    --paper: #ffffff;
    --reel-red: #e30613;
    --ink: #111111;
    --slate: #6e6c6c;
    --slate-edge: #1a1a1a;
    --web-grey: #4a4a4a;
    --figure-dark: #0c0c0c;
    --figure-mid: #2e2e2e;
  }
  html, body {
    margin: 0;
    padding: 0;
    overflow: hidden;
    background: var(--paper);
  }
  .poster {
    display: block;
    width: 1019px;
    height: 1200px;
    background: var(--paper);
  }
  .film-strip__band { fill: var(--reel-red); }
  .film-strip__hole { fill: var(--paper); }
  .figure-slot { fill: url(#figureTone); }
  .label-box { fill: var(--slate); stroke: var(--slate-edge); stroke-width: 5; }
  .label-box__text {
    fill: var(--paper);
    font-family: "Advent Pro", "Arial Narrow", sans-serif;
    font-weight: 200;
  }
  .headline {
    fill: var(--ink);
    font-family: "Oswald", "Arial Narrow", sans-serif;
    font-weight: 500;
  }
  .credit {
    fill: var(--ink);
    font-family: "Oswald", "Arial Narrow", sans-serif;
    font-weight: 600;
  }
  .web-address {
    fill: var(--web-grey);
    font-family: "Advent Pro", "Arial", sans-serif;
    font-weight: 300;
  }
</style>
</head>
<body>
<svg class="poster" viewBox="0 0 1019 1200" width="1019" height="1200" xmlns="http://www.w3.org/2000/svg">
  <defs>
    <pattern id="sprockets" patternUnits="userSpaceOnUse" width="56" height="300" x="0" y="-300">
      <rect class="film-strip__hole" x="18" y="10" width="24" height="15"/>
      <rect class="film-strip__hole" x="18" y="275" width="24" height="15"/>
    </pattern>
    <linearGradient id="figureTone" x1="0" y1="0" x2="0" y2="1">
      <stop offset="0" stop-color="var(--figure-dark)"/>
      <stop offset="1" stop-color="var(--figure-mid)"/>
    </linearGradient>
  </defs>

  <g class="film-strip" transform="translate(15 0) rotate(53.9)">
    <rect class="film-strip__band" x="-40" y="-300" width="1700" height="300"/>
    <rect x="-40" y="-300" width="1700" height="300" fill="url(#sprockets)"/>
  </g>

  <rect class="figure-slot" x="648" y="98" width="288" height="815" rx="40"
        role="img" aria-label="Illustration of an elegant woman in a wide black hat, sunglasses and little black dress walking along the red film strip"/>

  <rect class="label-box" x="41" y="465" width="250" height="168"/>
  <text class="label-box__text" x="62" y="610" font-size="170" textLength="208" lengthAdjust="spacingAndGlyphs">18TH</text>

  <text class="headline" x="42" y="701" font-size="52" textLength="294" lengthAdjust="spacingAndGlyphs">ANNUAL LARKS</text>
  <text class="headline" x="42" y="777" font-size="52" textLength="286" lengthAdjust="spacingAndGlyphs">FILM FESTIVAL</text>

  <rect class="label-box" x="41" y="802" width="250" height="102"/>
  <text class="label-box__text" x="64" y="884" font-size="92" textLength="200" lengthAdjust="spacingAndGlyphs">1/2/3</text>

  <text class="headline" x="42" y="978" font-size="56" textLength="184" lengthAdjust="spacingAndGlyphs">MAY 2015</text>

  <text class="credit" x="42" y="1034" font-size="27" textLength="570" lengthAdjust="spacingAndGlyphs">SCHOOL OF SCREEN AND DIGITAL STORYTELLING</text>
  <text class="credit" x="42" y="1070" font-size="27" textLength="251" lengthAdjust="spacingAndGlyphs">REDBROOK UNIVERSITY</text>
  <text class="credit" x="42" y="1106" font-size="27" textLength="255" lengthAdjust="spacingAndGlyphs">OTTO VRELAND CINEMA</text>

  <text class="web-address" x="43" y="1146" font-size="26" textLength="314" lengthAdjust="spacingAndGlyphs">www.larksreelweek.example</text>
</svg>
</body>
</html>
```